Student Profile

I would like to create a profile of .a few scholars at a primary school in South Africa. The profile is attached. I would like to it to be visually appealing for donors and to be in the same vein as the Thabeng Academy PDF. Please also find our branding guide and our logo. I've also included a few pictures that I would like for you to include.

Target Market(s)

Potential donors

Industry/Entity Type

School

Requirements
Must have
• Colours from the branding guide, photos

```html
<!DOCTYPE html>
<html lang="en">
<head>
<meta charset="utf-8">
<title>Thabeng Academy – Student &amp; Parent Profile</title>
<link href="https://fonts.googleapis.com/css2?family=Source+Sans+3:ital,wght@0,400;0,600;0,700;1,400;1,600&family=Gelasio:wght@600&display=swap" rel="stylesheet">
<style>
:root{
  --purple:#6a2c91;
  --green:#9fbf2e;
  --yellow:#f6c400;
  --blue:#1f6fb8;
  --cyan:#3cbde9;
  --navy:#1b3560;
  --white:#ffffff;
  --backdrop:#e6e6e4;
  --photo-warm:#b79478;
  --photo-cool:#3b4f7a;
}
*{margin:0;padding:0;box-sizing:border-box}
html,body{width:1200px;height:852px;overflow:hidden;background:var(--backdrop)}
body{position:relative;font-family:"Source Sans 3",Arial,sans-serif;color:var(--white)}
.page{position:absolute;top:86px;width:498px;height:644px;overflow:hidden;background:var(--white);box-shadow:0 3px 10px rgba(0,0,0,.25)}
.page--scholar{left:72px}
.page--parent{left:616px}
.page__shapes{position:absolute;inset:0}
.photo{position:absolute}
.text{position:absolute;font-size:8.2px;line-height:11.7px;text-align:justify}
.text p{margin-bottom:11.7px}
.text em{font-weight:600}

/* left page */
.brand{position:absolute;left:320px;top:44px;display:flex;align-items:center;gap:8px;color:var(--blue);font-size:19px;font-weight:600;letter-spacing:.5px}
.brand__dot{width:26px;height:26px;border-radius:50%;background:var(--blue)}
.profile-title{position:absolute;left:316px;top:106px;width:170px;text-align:center;color:var(--navy);font-weight:700;font-size:11px;line-height:17px}
.portrait{position:absolute;left:337px;top:149px;width:138px;height:138px;border-radius:50%;border:3px solid var(--white);background:radial-gradient(circle at 45% 40%,#8a6a55,#33456f 70%)}
.tagline{position:absolute;left:22px;top:218px;font-size:13.5px;line-height:18px}
.tagline strong{color:var(--yellow);font-weight:600}
.name-tag{position:absolute;left:22px;top:327px;font-size:11px}
.facts{position:absolute;left:22px;top:352px;font-size:10px;line-height:14px}
.facts .quote{color:var(--purple)}
.col{width:213px}
.col--a{left:22px;top:420px}
.col--b{left:267px;top:304px;width:215px}

/* right page */
.pull-quote{position:absolute;left:44px;top:138px;font-family:"Gelasio",Georgia,serif;font-weight:600;font-size:15.5px;line-height:18px}
.pull-quote__mark{position:absolute;left:-24px;top:-16px;color:var(--yellow);font-size:40px;line-height:40px}
.intro{left:19px;top:211px;width:215px}
.col--c{left:19px;top:315px;width:215px}
.col--d{left:267px;top:315px;width:215px}

/* footer */
.contact{position:absolute;right:18px;top:585px;text-align:right;font-size:8.6px;line-height:18.5px}
.contact li{list-style:none;display:flex;justify-content:flex-end;align-items:center;gap:5px}
.contact b{font-weight:700}
.contact svg{width:10px;height:10px}
</style>
</head>
<body>

<article class="page page--scholar">
  <svg class="page__shapes" viewBox="0 0 498 644" preserveAspectRatio="none">
    <defs>
      <linearGradient id="photoFadeL" x1="0" x2="1">
        <stop offset="0" stop-color="#8c7a6a"/>
        <stop offset=".45" stop-color="#4a5d8a"/>
        <stop offset=".66" stop-color="#c9b8ac"/>
        <stop offset=".78" stop-color="#ffffff"/>
      </linearGradient>
    </defs>
    <rect class="photo-fill" role="img" aria-label="Photo of a smiling young scholar on a playground swing" x="0" y="0" width="498" height="216" fill="url(#photoFadeL)"/>
    <polygon points="0,188 498,212 498,216 0,311" fill="var(--purple)"/>
    <polygon points="0,311 498,216 498,644 0,644" fill="var(--green)"/>
    <polygon points="0,322 198,322 188,346 0,346" fill="var(--cyan)"/>
    <polygon points="0,551 136,618 0,644" fill="var(--yellow)"/>
    <polygon points="0,640 498,549 498,556 0,644" fill="var(--white)"/>
    <polygon points="0,644 498,556 498,644" fill="var(--blue)"/>
  </svg>

  <div class="brand"><span class="brand__dot"></span>THABENG ACADEMY</div>
  <h1 class="profile-title">THABENG ACADEMY<br>STUDENT &amp; PARENT PROFILE</h1>
  <div class="portrait" role="img" aria-label="Round portrait photo of the scholar smiling"></div>

  <p class="tagline">Supporting both scholars and their<br>parents to <strong>‘SET THEIR DREAMS FREE’</strong></p>

  <p class="name-tag">Scholar’s Name: Naledi, or “Ledi”</p>
  <div class="facts">
    <p>Grade: 1</p>
    <p>Age: 6 years old</p>
    <p>Favorite thing to learn at school:&nbsp; Math because</p>
    <p class="quote">“it helps me to grow my brain”.</p>
  </div>

  <div class="text col col--a">
    <p>Naledi, or Ledi, as she likes to be called, loves to read. Her favourite book is Tilly’s Little Sister by Ann Mercer. Ledi’s vivid imagination and confidence (she loves playing teacher too) thrive thanks to the safe, nurturing and containing environment at Thabeng Academy.</p>
    <p>Ledi feels seen and heard: <em>“My teachers always teach me and they believe in me and tell me every chance they get.”</em></p>
    <p>Ledi’s confidence is a skill she feels she’s honed at Thabeng Academy. It’s certainly love and respect that has</p>
  </div>

  <div class="text col col--b">
    <p>allowed Ledi to blossom. Ledi’s confidence is a skill she feels she’s honed at Thabeng Academy. It’s certainly love and respect that has allowed Ledi to blossom. At only six years old, Ledi says she has learned to love herself and others more. She brings this emotional attunement along with the other critical knowledge and skills that she has gained at Thabeng to her life experiences both within and outside of school.</p>
    <p>Ledi lives in a two-room house on 5th Avenue in Riverside township with her mother, Grace, and two brothers, Sipho and Kabelo. While Grace earns enough to send her children to school and pay for the transport there, there isn’t much left and it is her alone who bears the cost of raising children. Grace’s husband was in an accident and he is no longer able to work as a builder.</p>
    <p>However, Grace is determined to send her three children to private schools like Thabeng Academy because local government schools are no alternatives.</p>
  </div>

  <ul class="contact">
    <li>+27 11 555 0142 <svg viewBox="0 0 10 10"><circle cx="5" cy="5" r="4.4" fill="none" stroke="var(--yellow)"/><path d="M3.4 3c.3 1.8 1.5 3.2 3.4 3.8l.6-.8-1-.6-.5.4C5.2 5.5 4.6 4.9 4.3 4.1l.4-.5-.6-1z" fill="var(--yellow)"/></svg></li>
    <li>giving@thabengacademy.org <svg viewBox="0 0 10 10"><circle cx="5" cy="5" r="4.4" fill="none" stroke="var(--yellow)"/><rect x="2.8" y="3.5" width="4.4" height="3" fill="none" stroke="var(--yellow)" stroke-width=".8"/><path d="M2.8 3.5 5 5.2 7.2 3.5" fill="none" stroke="var(--yellow)" stroke-width=".7"/></svg></li>
    <li><b>www.thabengacademy.org</b> <svg viewBox="0 0 10 10"><circle cx="5" cy="5" r="4.4" fill="none" stroke="var(--yellow)"/><circle cx="5" cy="5" r="2.4" fill="none" stroke="var(--yellow)" stroke-width=".8"/><path d="M2.6 5h4.8M5 2.6v4.8" stroke="var(--yellow)" stroke-width=".6"/></svg></li>
  </ul>
</article>

<article class="page page--parent">
  <svg class="page__shapes" viewBox="0 0 498 644" preserveAspectRatio="none">
    <defs>
      <linearGradient id="photoFadeR" x1="0" x2="1">
        <stop offset="0" stop-color="#c4b2a6"/>
        <stop offset=".5" stop-color="#8a6c5e"/>
        <stop offset="1" stop-color="#5d6a58"/>
      </linearGradient>
    </defs>
    <rect role="img" aria-label="Photo of the scholar's mother smiling beside her son on a swing" x="0" y="0" width="498" height="310" fill="url(#photoFadeR)"/>
    <polygon points="0,0 80,0 344,234 216,302 0,302" fill="var(--purple)"/>
    <polygon points="216,302 498,171 498,250" fill="var(--yellow)"/>
    <polygon points="0,302 216,302 498,250 498,644 0,644" fill="var(--green)"/>
    <polygon points="0,551 136,618 0,644" fill="var(--yellow)"/>
    <polygon points="0,640 498,549 498,556 0,644" fill="var(--white)"/>
    <polygon points="0,644 498,556 498,644" fill="var(--blue)"/>
  </svg>

  <blockquote class="pull-quote"><span class="pull-quote__mark">“</span>My mom tells me<br>I can be anything<br>I want to be.”</blockquote>

  <div class="text intro">
    <p>Indeed, Ledi wants to be many things. She wants to be a chef to help her mom with the cooking and, she wants to teach. She says her students will attend Ridgeview University after they finish school! Currently, Ledi enjoys helping other scholars with their class work, especially those struggling with math.</p>
  </div>

  <div class="text col col--c">
    <p>Grace’s hopes and dreams for her children arise from the deep love she feels for them as well as her own thwarted schooling dreams.</p>
    <p>“I was always number one in my class, and I especially loved accounting, but my mother didn’t really understand,” says Grace. Grace grew up hungry and said she didn’t get much adult support and encouragement. She dropped out in Grade 10, but still looked for piece work to support her studies. Grace moved to Johannesburg from Limpopo with her partner at the time to seek a new life. It was harder than she expected, compounded by her partner’s incapacity to work due to mental illness.</p>
    <p>Grace supported them both on a domestic worker’s salary. Tenacious little Ledi loves her mom and cherishes the time they spend reading books and doing Ledi’s math homework. After Ledi herself completes her university studies, she wants to live in Cape Town.</p>
  </div>

  <div class="text col col--d">
    <p>“Cape Town makes me feel very happy,” she says.</p>
    <p>A university preparatory school located in the Riverside Township of Johannesburg, South Africa, Thabeng Academy not only equips its scholars with the tools they need to achieve academic success, but also provides them with the skills necessary to succeed in life. This includes intentionally creating a nurturing and enabling environment where respect for oneself and others, self-confidence, and resiliency are equally developed and valued alongside the key learning and academic skills that are foundational for students on the path to university.</p>
    <p><em><i>“Thabeng Academy was founded so that children like Ledi can dream with their eyes wide opened! We are delighted to watch Ledi and her peers grow into such thoughtful and intelligent little beings”,</i></em> says Thabeng Academy co-founder Nomsa Dlamini-Reed</p>
  </div>

  <ul class="contact">
    <li>+27 11 555 0142 <svg viewBox="0 0 10 10"><circle cx="5" cy="5" r="4.4" fill="none" stroke="var(--yellow)"/><path d="M3.4 3c.3 1.8 1.5 3.2 3.4 3.8l.6-.8-1-.6-.5.4C5.2 5.5 4.6 4.9 4.3 4.1l.4-.5-.6-1z" fill="var(--yellow)"/></svg></li>
    <li>giving@thabengacademy.org <svg viewBox="0 0 10 10"><circle cx="5" cy="5" r="4.4" fill="none" stroke="var(--yellow)"/><rect x="2.8" y="3.5" width="4.4" height="3" fill="none" stroke="var(--yellow)" stroke-width=".8"/><path d="M2.8 3.5 5 5.2 7.2 3.5" fill="none" stroke="var(--yellow)" stroke-width=".7"/></svg></li>
    <li><b>www.thabengacademy.org</b> <svg viewBox="0 0 10 10"><circle cx="5" cy="5" r="4.4" fill="none" stroke="var(--yellow)"/><circle cx="5" cy="5" r="2.4" fill="none" stroke="var(--yellow)" stroke-width=".8"/><path d="M2.6 5h4.8M5 2.6v4.8" stroke="var(--yellow)" stroke-width=".6"/></svg></li>
  </ul>
</article>

</body>
</html>
```